National appliance rental company needs a newspaper ad design

We need an ad template that we can use for different newspaper advertising. Ad is to be colourful - I have attached our current marketing so you have an idea of colours.
Text to be something like the below:

Want it, Rent it, Own it!

Need to update your furniture? Kids need stuff for school?

(Put in pics of phones and TV)

Tablix starting from just $8 per week
Smart phones starting from $10 per week
Large family fridges from $30 per week

TV’s, laptops, whitegoods, furniture, beds – we will finance just about anything!

Fast approvals – call 1300 582 961 or go to www.brightgoodshire.example.au/apply - NOW!
$50 credit voucher given to the first 10 successful applicants.

(Pic of logo somewhere)
Terms and conditions apply. Pricing based on 24 month term

Harbourline Goods Hire P/L ACN 061 247 893. Australian Credit Licence # 718294

Target Market(s)

Low income people and families

Industry/Entity Type

Appliance

Requirements
Must have
• I would love to have a couple of different sizes.
• Maybe 6cm x 10 cm, and also 10cms x 10cms.
Nice to have
• Please use the green from fridge magnet and colours from our logo, etc.

```html
<!DOCTYPE html>
<html lang="en">
<head>
<meta charset="utf-8">
<title>Harbourline Goods Hire – Newspaper Ad</title>
<link rel="stylesheet" href="https://fonts.googleapis.com/css2?family=Fredoka:wght@600&family=Arimo:ital,wght@0,400;0,700;1,400&display=swap">
<style>
  :root{
    --page:#e9e4dc;
    --orange:#f08a1e;
    --orange-deep:#e2531d;
    --yellow:#ffd21f;
    --sun:#ffe27a;
    --red:#d92128;
    --red-deep:#c41a22;
    --blue:#1a84c9;
    --green:#75b93a;
    --ink:#2a2a2a;
    --white:#ffffff;
    --device:#1c1c1e;
  }
  *{box-sizing:border-box;margin:0;padding:0}
  html,body{width:1200px;height:1000px;overflow:hidden;background:var(--page)}
  .ad{
    position:absolute;left:152px;top:52px;width:896px;height:896px;overflow:hidden;
    background:radial-gradient(circle at 42% 28%, var(--sun) 0%, var(--yellow) 18%, var(--orange) 55%, var(--orange-deep) 100%);
    font-family:"Arimo",Arial,sans-serif;
  }
  .mascot{position:absolute;left:53px;top:10px;width:175px;height:230px;border-radius:22px;
    background:linear-gradient(180deg,#ffffff,#d9dde2)}
  .brand{position:absolute;left:218px;top:62px;width:330px;text-align:center}
  .brand-name{font-weight:700;color:var(--red);font-size:46px;line-height:50px}
  .brand-tagline{margin-top:10px;font-style:italic;font-size:17px;color:var(--ink)}
  .phones{position:absolute;left:586px;top:13px;width:287px;height:200px;border-radius:18px;
    background:linear-gradient(135deg,#e8ecf0 0%,#2b2b2e 45%,#1f5fa8 100%)}
  .tv{position:absolute;left:608px;top:183px;width:240px;height:245px;border-radius:6px;
    background:linear-gradient(160deg,#3a3a3d,var(--device) 60%,#000)}
  .headline{position:absolute;left:0;top:243px;width:606px;text-align:center;
    font-family:"Fredoka",sans-serif;font-weight:600;font-size:80px;line-height:86px;
    color:var(--red);-webkit-text-stroke:12px var(--white);paint-order:stroke fill;
    text-shadow:0 3px 6px rgba(0,0,0,.3)}
  .subtext{position:absolute;left:0;top:444px;width:610px;text-align:center;
    font-weight:700;font-size:17px;line-height:22px;color:var(--ink)}
  .offer{position:absolute;left:15px;width:313px;height:66px;border:3px solid var(--white);
    border-radius:10px;color:var(--white);font-size:23px;line-height:27px;padding:4px 0 0 22px}
  .offer b{color:var(--yellow);font-weight:700}
  .offer-red{top:511px;background:var(--red)}
  .offer-blue{top:586px;background:var(--blue)}
  .offer-green{top:660px;background:var(--green)}
  .finance{position:absolute;left:340px;top:511px;width:290px;height:215px;background:var(--blue);
    border:3px solid var(--white);border-radius:10px;color:var(--white);font-size:21px;line-height:29px;
    text-align:center;padding:16px 70px 0 14px}
  .voucher{position:absolute;left:593px;top:438px;width:340px;height:340px;border-radius:50%;
    background:var(--yellow);border:4px solid var(--white)}
  .voucher-text{position:absolute;left:612px;top:520px;width:280px;text-align:center;
    color:var(--red);font-weight:700;font-size:32px;line-height:39px}
  .approvals{position:absolute;left:0;top:741px;width:896px;height:85px;background:var(--green);
    border-top:3px solid var(--white);text-align:center}
  .approvals-title{margin-top:8px;font-weight:700;font-size:30px;color:var(--red);
    -webkit-text-stroke:5px var(--white);paint-order:stroke fill;line-height:34px}
  .approvals-contact{font-size:21px;color:var(--ink);margin-top:5px}
  .approvals-contact b{font-weight:700}
  .legal{position:absolute;left:0;top:826px;width:896px;height:70px;background:var(--red-deep);
    color:var(--white);text-align:center;font-size:17px;line-height:23px;padding-top:12px}
</style>
</head>
<body>
<div class="ad">
  <div class="mascot" role="img" aria-label="Cartoon fridge mascot waving"></div>
  <div class="brand">
    <div class="brand-name">Harbourline Goods Hire</div>
    <div class="brand-tagline">“It’s cheaper to hire smart!”</div>
  </div>
  <div class="phones" role="img" aria-label="Three smartphones fanned out"></div>
  <div class="tv" role="img" aria-label="Flat screen television"></div>

  <h1 class="headline">Want it, Rent it,<br>Own it!</h1>
  <p class="subtext">Need to update your furniture?<br>Kids need stuff for school?</p>

  <div class="offer offer-red">Tablix starting from<br>just <b>$8</b> per week</div>
  <div class="offer offer-blue">Smart phones starting<br>from <b>$10</b> per week</div>
  <div class="offer offer-green">Large family fridges<br>from <b>$30</b> per week</div>

  <div class="finance">TV’s, laptops, whitegoods, furniture, beds – we will finance just about anything!</div>

  <div class="voucher"></div>
  <div class="voucher-text">$50 credit voucher given to the first 10 successful applicants.</div>

  <div class="approvals">
    <div class="approvals-title">FAST APPROVALS</div>
    <div class="approvals-contact">call <b>1300 582 961</b> or go to www.brightgoodshire.example.au/apply - <b>NOW!</b></div>
  </div>
  <div class="legal">Terms and conditions apply. Pricing based on 24 month term<br>Harbourline Goods Hire P/L ACN 061 247 893. Australian Credit Licence # 718294</div>
</div>
</body>
</html>
```